Bref créative
Environmental Company Bus Card
Kestrel Ecological Bus Card
Professional
Derek Malloy
Director of Operations
418 Fenwick Park Rd Suite B
Brackenford, MD 21890
derek@kestrelecological.com
www.kestrelecological.com
I would like a fairly standard, but flashy/eye catching business card, with the logo and business name on the back of the card.
The card must have the required printing "bleed" around all edges. This wasn't done on the last project.
The logo shows the business name underneath of it. It does not have to be this way. The triangle logo can be the important feature, while the business name can be moved around wherever it is best suited.
Here is the logo file.
Here is the brochure file to see our color scheme and current design choice.

```html
<!DOCTYPE html>
<html lang="en">
<head>
<meta charset="utf-8">
<title>Kestrel Ecological — Business Card</title>
<link rel="stylesheet" href="https://fonts.googleapis.com/css2?family=Cinzel:wght@400;600&family=Lato:wght@400;700&display=swap">
<style>
  :root {
    --page: #e9ebee;
    --card: #ffffff;
    --blue: #2f86c0;
    --blue-deep: #1d5f95;
    --blue-light: #4ea3d8;
    --charcoal: #2e3136;
    --grey-text: #5d646c;
    --shadow: rgba(20, 30, 45, 0.18);
  }
  * { box-sizing: border-box; margin: 0; padding: 0; }
  html, body {
    width: 1200px;
    height: 864px;
    overflow: hidden;
    background: var(--page);
  }
  .stage {
    position: relative;
    width: 1200px;
    height: 864px;
  }
  .card {
    position: absolute;
    width: 520px;
    height: 300px;
    border-radius: 18px;
    background: var(--card);
    overflow: hidden;
    box-shadow: 0 14px 30px var(--shadow);
  }
  .card--back { left: 60px; top: 150px; }
  .card--front { left: 620px; top: 414px; }

  /* Back side */
  .back-brand {
    position: absolute;
    left: 0; right: 0; top: 104px;
    display: flex;
    align-items: center;
    justify-content: center;
    gap: 14px;
  }
  .brand-dot {
    width: 30px; height: 30px;
    border-radius: 50%;
    background: var(--blue);
  }
  .brand-name {
    font-family: "Cinzel", serif;
    font-weight: 600;
    color: var(--blue);
    font-size: 28px;
    letter-spacing: 1px;
  }
  .back-web {
    position: absolute;
    left: 0; right: 0; top: 166px;
    text-align: center;
    font-family: "Cinzel", serif;
    font-size: 12px;
    letter-spacing: 3px;
    color: var(--grey-text);
  }

  /* Front side */
  .front-art { position: absolute; inset: 0; }
  .front-identity {
    position: absolute;
    left: 36px; top: 62px;
    width: 250px;
  }
  .front-identity .brand-dot { display: block; width: 22px; height: 22px; margin-bottom: 14px; }
  .front-company {
    font-family: "Cinzel", serif;
    font-weight: 600;
    font-size: 20px;
    line-height: 1.2;
    color: var(--blue);
  }
  .front-person {
    margin-top: 40px;
    font-family: "Cinzel", serif;
    font-weight: 600;
    font-size: 15px;
    letter-spacing: 1px;
    color: var(--blue);
  }
  .front-title {
    margin-top: 4px;
    font-family: "Cinzel", serif;
    font-size: 11px;
    letter-spacing: 1px;
    color: var(--grey-text);
  }
  .contact-list {
    position: absolute;
    right: 26px; top: 78px;
    list-style: none;
    text-align: right;
    font-family: "Lato", sans-serif;
    font-size: 11px;
    line-height: 1.75;
    color: #ffffff;
    letter-spacing: 0.4px;
  }
</style>
</head>
<body>
<main class="stage">

  <section class="card card--back" aria-label="Business card back">
    <div class="back-brand">
      <span class="brand-dot"></span>
      <span class="brand-name">Kestrel Ecological</span>
    </div>
    <p class="back-web">www.kestrelecological.com</p>
  </section>

  <section class="card card--front" aria-label="Business card front">
    <svg class="front-art" width="520" height="300" viewBox="0 0 520 300" aria-hidden="true">
      <defs>
        <linearGradient id="panelBlue" x1="0" y1="0" x2="1" y2="1">
          <stop offset="0" stop-color="#4ea3d8"/>
          <stop offset="0.55" stop-color="#2f86c0"/>
          <stop offset="1" stop-color="#1d5f95"/>
        </linearGradient>
      </defs>
      <path d="M318,0 Q250,140 284,300 L520,300 L520,0 Z" fill="#2e3136"/>
      <path d="M330,0 Q262,140 296,300 L520,300 L520,0 Z" fill="#ffffff"/>
      <path d="M344,0 Q278,140 310,300 L520,300 L520,0 Z" fill="url(#panelBlue)"/>
    </svg>

    <div class="front-identity">
      <span class="brand-dot"></span>
      <h1 class="front-company">Kestrel Ecological, LLC</h1>
      <p class="front-person">Derek Malloy</p>
      <p class="front-title">Director of Operations</p>
    </div>

    <ul class="contact-list">
      <li>418 Fenwick Park Rd Suite B</li>
      <li>Brackenford, MD 21890</li>
      <li>P 410.555.0142</li>
      <li>F 410.555.0187</li>
      <li>derek@kestrelecological.com</li>
      <li>www.kestrelecological.com</li>
    </ul>
  </section>

</main>
</body>
</html>
```